Web Header needed for an inspirational coaching company's website - ongoing work

We need a beautifully designed web header to replace my current one at my homepage on my website www.brekavol.com
There will be continuous work required for various creative work in the future if your work is selected.
I work with corporate professionals and executives to bring clarity and joy back to their career. It needs to be elegant, sophisticated, intelligent, but friendly and inspiring at the same time.
Brief and the sample header size are attached in my files
Thank you!
Target Market(s)
Corporate profesionals and executives
Industry/Entity Type
It Company
Colors
Designer to choose colors to be used in the design.
Look and feel
Each slider illustrates characteristics of the customer's brand and the style your logo design should communicate.

```html
<!DOCTYPE html>
<html lang="en">
<head>
<meta charset="UTF-8">
<title>Career Partner Web Header</title>
<link rel="stylesheet" href="https://fonts.googleapis.com/css2?family=Playfair+Display:wght@500;600&family=Arimo:wght@700&display=swap">
<style>
  :root {
    --stage: #565656;
    --mist: #cfdedf;
    --slate: #879a9b;
    --frame: #9aabad;
    --name-ink: #8e9fa1;
    --sub-ink: #7f9092;
    --headline: #ffffff;
    --quote: #c9d6d6;
    --photo-light: #f1f3f3;
    --photo-mid: #dde3e4;
  }
  html, body {
    margin: 0;
    padding: 0;
    width: 1200px;
    height: 1200px;
    overflow: hidden;
    background: var(--stage);
  }
  .canvas {
    position: relative;
    width: 1200px;
    height: 1200px;
  }
  .web-header {
    position: absolute;
    left: 0;
    top: 383px;
    width: 1200px;
    height: 435px;
    display: block;
  }
  .bg-light { fill: var(--mist); }
  .bg-dark { fill: var(--slate); }
  .name-frame { fill: none; stroke: var(--frame); stroke-width: 3; }
  .coach-name {
    font-family: "Playfair Display", serif;
    font-weight: 600;
    font-size: 33px;
    fill: var(--name-ink);
  }
  .coach-title {
    font-family: "Arimo", Arial, sans-serif;
    font-weight: 700;
    font-size: 15px;
    fill: var(--sub-ink);
  }
  .headline {
    font-family: "Playfair Display", serif;
    font-weight: 500;
    font-size: 78px;
    fill: var(--headline);
  }
  .tagline {
    font-family: "Arimo", Arial, sans-serif;
    font-weight: 700;
    font-size: 24px;
    letter-spacing: 1px;
    fill: var(--quote);
  }
</style>
</head>
<body>
<div class="canvas">
  <svg class="web-header" viewBox="0 0 1200 435" xmlns="http://www.w3.org/2000/svg">
    <defs>
      <clipPath id="header-clip"><rect x="0" y="0" width="1200" height="435"/></clipPath>
      <radialGradient id="portrait-tone" cx="50%" cy="40%" r="60%">
        <stop offset="0%" stop-color="var(--photo-light)"/>
        <stop offset="100%" stop-color="var(--photo-mid)"/>
      </radialGradient>
    </defs>
    <g clip-path="url(#header-clip)">
      <rect class="bg-light" x="0" y="0" width="1200" height="435"/>
      <polygon class="bg-dark" points="750,0 1200,0 1200,435 317,435"/>

      <g class="portrait" role="img" aria-label="Portrait photo of the coach smiling, in an orange top, in a bright office">
        <circle cx="467" cy="269" r="162" fill="url(#portrait-tone)"/>
      </g>

      <g class="name-block">
        <polyline class="name-frame" points="293,287 68,287 68,359 320,359"/>
        <text class="coach-name" x="190" y="328" text-anchor="middle">MIRA TOLEV</text>
        <text class="coach-title" x="190" y="350" text-anchor="middle">Master of Coaching Psychology</text>
      </g>

      <g class="headline-block">
        <text class="headline" x="917" y="208" text-anchor="middle" textLength="236" lengthAdjust="spacing">YOUR</text>
        <text class="headline" x="917" y="272" text-anchor="middle" textLength="354" lengthAdjust="spacing">CAREER</text>
        <text class="headline" x="917" y="336" text-anchor="middle" textLength="415" lengthAdjust="spacing">PARTNER</text>
        <text class="tagline" x="917" y="379" text-anchor="middle">“Bring clarity to your career.”</text>
      </g>
    </g>
  </svg>
</div>
</body>
</html>
```